R&T Builders and Spaces Business Card

We need to redesign our business card. We had used white vellum wih grey logo and txt in the past. I would like to bring a little life into our cards without being over the top. I think I will be going away from the vellum and printing soft touch business cards.
I have attached what we currently have and our new logo design.

```html
<!DOCTYPE html>
<html lang="en">
<head>
<meta charset="utf-8">
<title>R&amp;T Builders and Spaces – Business Cards</title>
<link href="https://fonts.googleapis.com/css2?family=Jost:wght@400;500;600&display=swap" rel="stylesheet">
<style>
  :root {
    --page: #ffffff;
    --charcoal: #2b2b2b;
    --slate: #5b5b5d;
    --orange: #f37521;
    --light-ink: #ffffff;
    --dark-ink: #2a2a2a;
    --shadow: rgba(0, 0, 0, 0.28);
  }
  * { margin: 0; padding: 0; box-sizing: border-box; }
  html, body {
    width: 840px;
    height: 1200px;
    overflow: hidden;
    background: var(--page);
    font-family: "Jost", "Futura", sans-serif;
  }
  .sheet {
    position: relative;
    width: 840px;
    height: 1200px;
  }
  .card {
    position: absolute;
    left: 70px;
    width: 700px;
    height: 400px;
    box-shadow: 8px 10px 12px var(--shadow);
  }
  .card--dark { top: 160px; background: var(--charcoal); color: var(--light-ink); }
  .card--bright { top: 640px; background: var(--orange); color: var(--dark-ink); }

  .contact {
    position: absolute;
    right: 369px;
    top: 62px;
    text-align: right;
    text-transform: uppercase;
    font-size: 16px;
    line-height: 1.4;
    font-weight: 400;
  }
  .contact__name {
    font-size: 27px;
    font-weight: 600;
    letter-spacing: 0.02em;
    line-height: 1.1;
  }
  .contact__title { font-size: 17px; margin-bottom: 24px; }
  .contact__group { margin-bottom: 22px; }
  .contact__phones span + span { margin-left: 14px; }

  .brand-block {
    position: absolute;
    left: 357px;
    top: 56px;
    width: 255px;
    height: 255px;
    background: var(--slate);
  }
  .brand-name {
    position: absolute;
    left: 357px;
    top: 322px;
    font-size: 21px;
    font-weight: 400;
    letter-spacing: 0.06em;
    text-transform: uppercase;
    white-space: nowrap;
  }
</style>
</head>
<body>
<main class="sheet">
  <article class="card card--dark">
    <div class="contact">
      <p class="contact__name">Dana M. Whitcombe</p>
      <p class="contact__title">Principal</p>
      <div class="contact__group">
        <p>dana@rtbuilders.com</p>
        <p class="contact__phones"><span>T 555 014 2270</span><span>C 555 018 4431</span></p>
      </div>
      <div class="contact__group">
        <p>1180 W Alder St, Suite 200</p>
        <p>Mesa Vista, Arizona 85100</p>
      </div>
      <p>www.rtbuilders.com</p>
    </div>
    <div class="brand-block"></div>
    <p class="brand-name">R&amp;T Builders and Spaces</p>
  </article>

  <article class="card card--bright">
    <div class="contact">
      <p class="contact__name">Dana M. Whitcombe</p>
      <p class="contact__title">Principal</p>
      <div class="contact__group">
        <p>dana@rtbuilders.com</p>
        <p class="contact__phones"><span>T 555 014 2270</span><span>C 555 018 4431</span></p>
      </div>
      <div class="contact__group">
        <p>1180 W Alder St, Suite 200</p>
        <p>Mesa Vista, Arizona 85100</p>
      </div>
      <p>www.rtbuilders.com</p>
    </div>
    <div class="brand-block"></div>
    <p class="brand-name">R&amp;T Builders and Spaces</p>
  </article>
</main>
</body>
</html>
```